Wheels 4 Hire Car Co-Hosting program

I want to create an ad on Pictora, graphic design with my company name is Wheels 4 Hire . I am a host on the Vexa platform and I rent my cars out.
I have 90+ cars..
I’m trying to reach people that Have an extra car laying around or just tired of their car but are stuck with the payments.
And tell them Unlock earning potential with your car!
List it on our fleet for hassle-free renting on Vexa.
We manage A-Z and you profit.
Start now!
Dm us year, make, model and current mileage on odometer to find out if you qualify!
Vehicle must have a clean title and must be registered to you!

Target Market(s)

People that have an extra car laying around or are tired of their car and warm to get into a new car but they are stuck with the payments of their original car. We can take their car and rent it out for them.

Industry/Entity Type

Car rental fleet management

Requirements
Must have
• Car rental, money, profit, etc

```html
<!DOCTYPE html>
<html lang="en">
<head>
<meta charset="utf-8">
<title>Wheels 4 Hire – Co-Hosting Ad</title>
<link rel="stylesheet" href="https://fonts.googleapis.com/css2?family=Montserrat:ital,wght@0,700;0,800;0,900;1,600;1,700&family=Arimo:wght@700&display=swap">
<style>
  :root {
    --blue: #0745dd;
    --yellow: #ffe000;
    --ink: #0a0a0a;
    --white: #ffffff;
    --cash: #c9cfbd;
    --car-tone: #9aa3ad;
  }
  * { margin: 0; padding: 0; box-sizing: border-box; }
  html, body { width: 960px; height: 1200px; overflow: hidden; background: var(--white); }
  .ad {
    position: relative; width: 960px; height: 1200px; overflow: hidden;
    background: var(--white); font-family: "Montserrat", sans-serif; color: var(--ink);
  }
  .blue-sweep { position: absolute; left: 0; top: 0; width: 960px; height: 1200px; }
  .cash {
    position: absolute; background: linear-gradient(135deg, #dfe3d6, var(--cash));
    border-radius: 4px; opacity: .85;
  }
  .brand {
    position: absolute; top: 16px; left: 0; width: 960px; text-align: center;
    font-weight: 900; font-size: 32px; letter-spacing: 1px; color: var(--ink);
  }
  .unlock {
    position: absolute; left: 330px; top: 102px; width: 290px; height: 87px;
    background: var(--yellow); border-radius: 6px;
    font-weight: 800; font-size: 66px; line-height: 87px; text-align: center;
  }
  .lock-badge { position: absolute; left: 582px; top: 64px; width: 62px; height: 62px; }
  .headline {
    position: absolute; left: 0; width: 960px; text-align: center;
    font-weight: 900; line-height: 1; letter-spacing: -2px;
  }
  .headline--earning { top: 190px; font-size: 124px; }
  .headline--potential { top: 296px; font-size: 124px; letter-spacing: -3px; }
  .tagline-row {
    position: absolute; top: 403px; left: 0; width: 960px; height: 86px;
    display: flex; justify-content: center; align-items: center; gap: 14px;
  }
  .with-your {
    font-weight: 800; font-size: 76px; line-height: 86px; letter-spacing: -2px; white-space: nowrap;
  }
  .car-tag {
    height: 86px; padding: 0 12px;
    background: var(--yellow); border-radius: 6px;
    font-weight: 900; font-size: 78px; line-height: 86px; letter-spacing: -2px; white-space: nowrap;
  }
  .fleet-photo {
    position: absolute; left: 40px; top: 505px; width: 868px; height: 192px;
    border-radius: 60px 60px 24px 24px;
    background: linear-gradient(180deg, #c4cad1 0%, var(--car-tone) 60%, #5c636b 100%);
  }
  .promise {
    position: absolute; top: 712px; left: 0; width: 960px; text-align: center;
    color: var(--white); font-weight: 800; font-size: 47px; letter-spacing: -.5px; white-space: nowrap;
  }
  .promise-underline { position: absolute; left: 700px; top: 768px; width: 200px; height: 14px; }
  .fleet-box {
    position: absolute; left: 151px; top: 801px; width: 658px; height: 114px;
    background: var(--white); border-radius: 14px;
    box-shadow: 0 10px 18px rgba(0,0,0,.18);
    font-style: italic; font-weight: 700; font-size: 42px; line-height: 42px;
    text-align: center; padding-top: 14px; white-space: nowrap;
  }
  .fleet-box .platform { font-style: normal; font-weight: 800; letter-spacing: 1px; }
  .cta {
    position: absolute; left: 263px; top: 939px; width: 437px; height: 73px;
    background: var(--yellow); border-radius: 37px;
    font-weight: 800; font-size: 55px; line-height: 73px; text-align: center; letter-spacing: -1px;
  }
  .instructions {
    position: absolute; top: 1032px; left: 0; width: 960px; text-align: center;
    color: var(--white); font-family: "Arimo", sans-serif; font-weight: 700;
    font-size: 37px; line-height: 37px; white-space: nowrap;
  }
  .fine-print {
    position: absolute; top: 1131px; left: 0; width: 960px; text-align: center;
    color: var(--white); font-family: "Arimo", sans-serif; font-weight: 700;
    font-size: 24px; text-decoration: underline; white-space: nowrap;
  }
</style>
</head>
<body>
<main class="ad">
  <svg class="blue-sweep" viewBox="0 0 960 1200" aria-hidden="true">
    <path d="M0 484 C 180 560, 520 600, 960 520 L960 1200 L0 1200 Z" fill="var(--blue)"/>
  </svg>

  <div class="cash" role="img" aria-label="Flying dollar bills" style="left:-20px;top:10px;width:170px;height:80px;transform:rotate(-35deg)"></div>
  <div class="cash" role="img" aria-label="Flying dollar bills" style="left:-30px;top:150px;width:110px;height:70px;transform:rotate(60deg)"></div>
  <div class="cash" role="img" aria-label="Flying dollar bills" style="left:880px;top:360px;width:110px;height:60px;transform:rotate(55deg)"></div>
  <div class="cash" role="img" aria-label="Flying dollar bills" style="left:890px;top:500px;width:100px;height:140px;transform:rotate(-20deg)"></div>
  <div class="cash" role="img" aria-label="Flying dollar bills" style="left:-20px;top:1090px;width:160px;height:80px;transform:rotate(25deg)"></div>

  <div class="brand">Wheels 4 Hire</div>

  <div class="unlock">Unlock</div>
  <svg class="lock-badge" viewBox="0 0 62 62" aria-hidden="true">
    <circle cx="31" cy="31" r="30" fill="var(--ink)"/>
    <path d="M33 28 v-6 a7 7 0 0 1 14 0 v3" fill="none" stroke="var(--white)" stroke-width="4" stroke-linecap="round"/>
    <rect x="18" y="28" width="22" height="17" rx="3" fill="var(--white)"/>
  </svg>

  <div class="headline headline--earning">EARNING</div>
  <div class="headline headline--potential">POTENTIAL</div>
  <div class="tagline-row">
    <span class="with-your">with your</span>
    <span class="car-tag">Car!</span>
  </div>

  <div class="fleet-photo" role="img" aria-label="Row of five rental cars: hatchback, sedans and a minivan"></div>

  <div class="promise">We manage A-Z and you profit.</div>
  <svg class="promise-underline" viewBox="0 0 200 14" aria-hidden="true">
    <path d="M2 9 C 60 4, 140 3, 198 8" fill="none" stroke="var(--white)" stroke-width="5" stroke-linecap="round"/>
  </svg>

  <div class="fleet-box">List it on our fleet for<br>hassle-free renting on <span class="platform">VEXA</span></div>

  <div class="cta">Start now!</div>

  <p class="instructions">Dm us year, make, model and current mileage<br>on odometer to find out if you qualify!</p>
  <p class="fine-print">*Vehicle must have a clean title and must be registered to you!</p>
</main>
</body>
</html>
```